Design the retail packaging for the future of men's skincare!

Tolvex seeks to make skincare accessible and easy for the 80% of men who don't take care of their skin today. We need someone to design our hero skincare solution set's shipping and retail box: The Ka(Lo). The set includes both our all-in-one moisturizer, the Duskwell (red cap), and our two-in-one facial cleanser and shave gel, the Vantorel (clear cap).

This will be at major retailers around the country as well as being shipped directly to our customers.

Please use our brand strategy, color, and visual guidelines, as well as fonts, which are attached. The box we're designing is similar to the zTablo 9, both in size and aesthetic, with the dimensions being: 6.5" L 3.75" W 2.5" D. We're inclined to have images of the bottles on the front (attached) similar to the zTablo but are open to other aesthetics.

Target Market(s)

middle to upper class men, all ethnicities, ages 18-60

Industry/Entity Type

Cosmetics

Other font styles liked:
• See attached fonts

Colors

Designer to choose colors to be used in the design.

Requirements
Must have
• dimensions must be 6.5" L 3.75" W 2.5" D. Must include the weights of the two products on the front (Duskwell: 1.7oz/50ml and Vantorel 3.4fl oz/100ml and the ingredients on the back (attached.) Please include the following logos: Made in USA, Dermatologically tested, certified vegan (plantwise league), recyclable, and quiet wren. We also need room for a barcode on the back.
Nice to have
• An aesthetic similar to the zTablo boxes. Featured ingredients: Duskwell (Vitamin C, Indian Ginseng, CBD (30mg), Vantorel (eucalyptus, rosehip, soap bark)

```html
<!DOCTYPE html>
<html lang="en">
<head>
<meta charset="utf-8">
<title>Tolvex — Retail Box Front Panel</title>
<link rel="stylesheet" href="https://fonts.googleapis.com/css2?family=Poppins:wght@400;500;600&display=swap">
<style>
  :root {
    --backdrop: #6b6b6b;
    --panel: #0d0d0d;
    --panel-edge: #1a1a1a;
    --ink: #ffffff;
    --ink-soft: #d9d9d9;
    --ink-faint: #9a9a9a;
    --leaf-green: #5a9e1c;
    --leaf-bright: #8fd63a;
    --water-blue: #3d7fb5;
    --skin: #b98a6e;
  }
  * { box-sizing: border-box; margin: 0; padding: 0; }
  html, body {
    width: 1200px; height: 900px; overflow: hidden;
    background: var(--backdrop);
    font-family: "Poppins", sans-serif;
  }
  .canvas {
    width: 1200px; height: 900px;
    display: flex; align-items: center; justify-content: center;
  }
  .box-front {
    width: 400px; height: 820px;
    background: linear-gradient(180deg, var(--panel-edge) 0%, var(--panel) 40%, var(--panel) 100%);
    display: flex; flex-direction: column; align-items: center;
    padding: 90px 36px 28px;
  }
  .brand-mark {
    display: flex; align-items: center; gap: 12px;
    color: var(--ink);
    font-weight: 500; font-size: 44px; letter-spacing: 6px;
    text-transform: uppercase;
  }
  .brand-mark__square {
    width: 18px; height: 18px; background: var(--ink);
  }
  .hero-visual {
    margin-top: 70px;
    width: 300px; height: 360px;
    border-radius: 50% 50% 42% 42%;
    background:
      radial-gradient(ellipse at 50% 30%, var(--skin) 0%, rgba(185,138,110,0.5) 28%, transparent 52%),
      radial-gradient(ellipse at 50% 78%, var(--leaf-bright) 0%, var(--leaf-green) 30%, transparent 58%),
      radial-gradient(circle at 50% 45%, rgba(61,127,181,0.55) 0%, rgba(61,127,181,0.15) 55%, transparent 72%);
  }
  .product-info {
    margin-top: auto;
    display: flex; flex-direction: column; align-items: center; gap: 8px;
    text-align: center;
  }
  .product-name {
    color: var(--ink); font-weight: 500; font-size: 24px; letter-spacing: 1px;
  }
  .tagline-band {
    background: var(--leaf-green);
    color: var(--ink);
    font-size: 14px; font-weight: 500;
    padding: 4px 10px;
  }
  .tagline-sub {
    color: var(--ink-soft); font-size: 14px; font-weight: 500;
  }
  .size-note {
    margin-top: 18px;
    color: var(--ink-faint); font-size: 10px; font-weight: 400;
  }
</style>
</head>
<body>
  <main class="canvas">
    <section class="box-front">
      <div class="brand-mark">
        <span class="brand-mark__square"></span>
        <span>Tolvex</span>
      </div>
      <div class="hero-visual" role="img" aria-label="Photo of a man splashing water on his face, with a green plant leaf in front and blue water splashes around"></div>
      <div class="product-info">
        <h1 class="product-name">TOLVEX</h1>
        <p class="tagline-band">Accessible And Easy For The 80% Of Men</p>
        <p class="tagline-sub">seeks to make skincare</p>
        <p class="size-note">1.7 oz and 3.4 fl oz set</p>
      </div>
    </section>
  </main>
</body>
</html>
```